Creative Brief
Marlow Stationery & Business Card
Professional
Gordon P. Marlow
President
3815 Fennimore Ave.
Columbus, GA 31947
gordon@marlowhaulers.com
www.marlowhaulersales.com

```html
<!DOCTYPE html>
<html lang="en">
<head>
<meta charset="utf-8">
<title>Marlow Hauler Sales – Stationery</title>
<link href="https://fonts.googleapis.com/css2?family=Open+Sans:wght@400;600;800&display=swap" rel="stylesheet">
<style>
  :root{
    --bg:#e4e1dd;
    --paper:#ffffff;
    --paper-shade:#f3f3f3;
    --dark:#262626;
    --dark-2:#3a3a3a;
    --red:#d8422b;
    --text:#333333;
    --muted:#777777;
    --ghost:rgba(200,60,45,.09);
  }
  *{box-sizing:border-box;margin:0;padding:0}
  html,body{width:1200px;height:713px;overflow:hidden}
  body{background:var(--bg);font-family:"Open Sans",Arial,sans-serif;color:var(--text);position:relative}
  .piece{position:absolute;background:var(--paper);box-shadow:0 2px 6px rgba(0,0,0,.25);overflow:hidden}
  .brand{font-family:"Open Sans",Arial,sans-serif;font-weight:800;color:var(--red);letter-spacing:.5px;display:flex;align-items:center;gap:5px;line-height:1}
  .brand .dot{border-radius:50%;background:var(--red);display:inline-block}
  .ghost{position:absolute;font-weight:800;color:var(--ghost);line-height:1;white-space:nowrap}
  .small{font-size:5px;line-height:1.55;color:var(--text);white-space:nowrap}
  .light{color:#ddd}
  .row{display:flex;align-items:center;gap:3px}
  .ico{width:5px;height:5px;flex:none}

  /* business cards */
  .card{width:127px;left:24px;border-radius:6px}
  .card-front{top:53px;height:110px;background:var(--dark);display:flex;align-items:center;justify-content:center}
  .card-front .stripe{position:absolute;left:0;right:0;bottom:0;height:5px;background:var(--red)}
  .card-back{top:180px;height:103px}
  .card-back .name{position:absolute;left:7px;top:38px;font-size:6px;font-weight:600;line-height:1.4;white-space:nowrap}
  .title{font-size:4.5px;color:var(--muted);font-weight:400}
  .card-back .divider{position:absolute;left:62px;top:20px;bottom:22px;width:1px;background:#ccc}
  .card-back .info{position:absolute;left:65px;top:22px;font-size:4px}
  .card-back .info .row{gap:2px}
  .card-back .info .ico{width:4px;height:4px}
  .card-back .strip{position:absolute;left:0;right:0;bottom:0;height:8px;background:var(--dark)}
  .card-back .strip i{position:absolute;right:0;top:0;bottom:0;width:45%;background:var(--red)}
  .card-alt{top:295px;height:113px}
  .card-alt .name{position:absolute;left:10px;top:14px;font-size:6px;font-weight:600;line-height:1.4;white-space:nowrap}
  .card-alt .addr{position:absolute;left:10px;top:46px}
  .card-alt .phones{position:absolute;left:80px;top:16px}
  .card-alt .strip{position:absolute;left:0;right:0;bottom:0;height:16px;background:var(--dark)}
  .card-alt .strip i{position:absolute;left:0;right:0;top:0;height:3px;background:var(--red)}
  .card-alt .web{position:absolute;left:10px;bottom:4px;color:#ddd;font-size:5px}

  /* letterhead */
  .letterhead{left:233px;top:53px;width:403px;height:600px;background:linear-gradient(180deg,#fff 0%,var(--paper-shade) 100%)}
  .band{position:absolute;left:0;right:0;top:0;background:var(--dark)}
  .letterhead .band{height:27px}
  .letterhead .band .brand{position:absolute;left:14px;top:7px;font-size:13px}
  .letterhead .addr{position:absolute;left:140px;top:5px}
  .letterhead .contact{position:absolute;left:230px;top:4px}
  .letterhead .ghost{left:50%;top:46%;transform:translate(-50%,-50%);font-size:70px}
  .foot{position:absolute;left:0;right:0;bottom:0;height:6px;background:var(--dark-2)}
  .foot i{position:absolute;right:0;top:0;bottom:0;background:var(--red)}
  .letterhead .foot i{width:40%}

  /* envelopes */
  .envelope{left:715px;width:456px}
  .env-front{top:53px;height:211px}
  .env-front .band{height:28px;border-bottom:3px solid var(--red)}
  .env-front .band .brand{position:absolute;left:14px;top:7px;font-size:13px}
  .env-front .addr{position:absolute;left:14px;top:36px}
  .env-front .ghost{left:62%;top:54%;transform:translate(-50%,-50%);font-size:52px}
  .env-front .foot{height:5px;background:transparent}
  .env-front .foot i{width:42%}
  .env-back{top:348px;height:216px;background:linear-gradient(180deg,#fff,var(--paper-shade))}
  .env-back svg{position:absolute;left:0;top:0}
  .env-back .brand{position:absolute;left:50%;top:24px;transform:translateX(-50%);font-size:14px}
</style>
</head>
<body>

<svg width="0" height="0" style="position:absolute" aria-hidden="true">
  <symbol id="i-phone" viewBox="0 0 10 10"><path d="M2 1h2l1 2-1 1c.6 1.2 1.4 2 2.6 2.6l1-1 2 1v2c0 .6-.4 1-1 1C4.5 9.6.4 5.5 1 2c0-.6.4-1 1-1z" fill="currentColor"/></symbol>
  <symbol id="i-mail" viewBox="0 0 10 10"><rect x="1" y="2.5" width="8" height="5" fill="none" stroke="currentColor"/><path d="M1 2.5l4 3 4-3" fill="none" stroke="currentColor"/></symbol>
  <symbol id="i-web" viewBox="0 0 10 10"><circle cx="5" cy="5" r="4" fill="none" stroke="currentColor"/><path d="M1 5h8M5 1c-2 2.5-2 5.5 0 8M5 1c2 2.5 2 5.5 0 8" fill="none" stroke="currentColor" stroke-width=".7"/></symbol>
  <symbol id="i-pin" viewBox="0 0 10 10"><path d="M5 1a3 3 0 0 1 3 3c0 2-3 5-3 5S2 6 2 4a3 3 0 0 1 3-3z" fill="currentColor"/></symbol>
</svg>

<!-- Business card: front -->
<section class="piece card card-front">
  <div class="brand" style="font-size:15px"><span class="dot" style="width:7px;height:7px"></span>Marlow</div>
  <span class="stripe"></span>
</section>

<!-- Business card: contact side -->
<section class="piece card card-back">
  <p class="name">Gordon P. Marlow<br><span class="title">President</span></p>
  <span class="divider"></span>
  <div class="info small">
    <div>3815 Fennimore Ave.</div>
    <div>Columbus, GA 31947</div>
    <div class="row"><svg class="ico" style="color:var(--red)"><use href="#i-phone"/></svg>706-555-0142</div>
    <div class="row"><svg class="ico" style="color:var(--red)"><use href="#i-phone"/></svg>706-555-0187</div>
    <div class="row"><svg class="ico" style="color:var(--red)"><use href="#i-phone"/></svg>706-555-0163</div>
    <div class="row"><svg class="ico" style="color:var(--red)"><use href="#i-mail"/></svg>gordon@marlowhaulers.com</div>
    <div class="row"><svg class="ico" style="color:var(--red)"><use href="#i-web"/></svg>www.marlowhaulersales.com</div>
  </div>
  <div class="strip"><i></i></div>
</section>

<!-- Business card: alternate side -->
<section class="piece card card-alt">
  <p class="name">Gordon P. Marlow<br><span class="title">President</span></p>
  <div class="addr small">
    <div>3815 Fennimore Ave.</div>
    <div>Columbus, GA 31947</div>
  </div>
  <div class="phones small">
    <div>T 706-555-0142</div>
    <div>C 706-555-0187</div>
    <div>F 706-555-0163</div>
  </div>
  <div class="strip"><i></i><span class="web row"><svg class="ico" style="color:var(--red)"><use href="#i-web"/></svg>www.marlowhaulersales.com</span></div>
</section>

<!-- Letterhead -->
<section class="piece letterhead">
  <header class="band">
    <div class="brand"><span class="dot" style="width:6px;height:6px"></span>Marlow</div>
    <div class="addr small light">
      <div class="row"><svg class="ico" style="color:var(--red)"><use href="#i-pin"/></svg>3815 Fennimore Ave.</div>
      <div style="padding-left:8px">Columbus, GA 31947</div>
    </div>
    <div class="contact small light">
      <div class="row"><svg class="ico" style="color:var(--red)"><use href="#i-phone"/></svg>706-555-0142</div>
      <div class="row"><svg class="ico" style="color:var(--red)"><use href="#i-mail"/></svg>gordon@marlowhaulers.com</div>
      <div class="row"><svg class="ico" style="color:var(--red)"><use href="#i-web"/></svg>www.marlowhaulersales.com</div>
    </div>
  </header>
  <div class="ghost" aria-hidden="true">Marlow</div>
  <footer class="foot"><i></i></footer>
</section>

<!-- Envelope: front -->
<section class="piece envelope env-front">
  <header class="band">
    <div class="brand"><span class="dot" style="width:6px;height:6px"></span>Marlow</div>
  </header>
  <div class="addr small">
    <div>3815 Fennimore Ave.</div>
    <div>Columbus, GA 31947</div>
    <div class="row" style="margin-top:3px"><svg class="ico" style="color:var(--red)"><use href="#i-phone"/></svg>706-555-0142</div>
    <div class="row"><svg class="ico" style="color:var(--red)"><use href="#i-mail"/></svg>gordon@marlowhaulers.com</div>
    <div class="row"><svg class="ico" style="color:var(--red)"><use href="#i-web"/></svg>www.marlowhaulersales.com</div>
  </div>
  <div class="ghost" aria-hidden="true">Marlow</div>
  <footer class="foot"><i></i></footer>
</section>

<!-- Envelope: back -->
<section class="piece envelope env-back">
  <svg width="456" height="90" viewBox="0 0 456 90" aria-hidden="true">
    <path d="M0 0H456V46L252 84Q228 90 204 84L0 46Z" fill="var(--dark)"/>
    <path d="M0 46L204 84Q228 90 252 84L456 46" fill="none" stroke="var(--red)" stroke-width="3"/>
  </svg>
  <div class="brand"><span class="dot" style="width:7px;height:7px"></span>Marlow</div>
</section>

</body>
</html>
```